Pinecrest Renovations - Get the creative juices going!!

Pinecrest does not do the actual renovation work. The company provides high end project management of renovation (primarily residential - with an eye toward commercial) The renovation work could look very different between projects. This company manages the work of contractors, architects and interior designers (either subcontracted directly by Pinecrest or hired by the client and entrusted to Pinecrest to manage). Clients are high end in the economic scale and the card needs to have a high end feel to it.

The owner is female, but the audience will be heavily slanted male. It should not be a "feminine" or "masculine" looking card. If anything, slant more on the masculine side. Clean, simple, yet creative and artistically appealing. The card design should complement and in no way compete with the logo.

When people think of our company: trust, integrity, dynamic, limitless possibilities, transition, energy, creative. We plan to expand in the future to be international.

There will also be a contest running for stationary. Please check that section, as well.

***Black is 80-90 percent black. Not stark black

Tight timeline. Needs cards printed quickly!

Residential

```html
<!DOCTYPE html>
<html lang="en">
<head>
<meta charset="utf-8">
<title>Pinecrest Renovations – Business Card</title>
<link href="https://fonts.googleapis.com/css2?family=Montserrat:wght@400;600;700&family=Roboto:wght@300;400&display=swap" rel="stylesheet">
<style>
  :root {
    --teal: #00a39b;
    --ink: #2b2a2c;
    --ink-soft: #4a4a4c;
    --paper: #ffffff;
    --backdrop: #e8e5e0;
  }
  * { box-sizing: border-box; margin: 0; padding: 0; }
  html, body {
    width: 1200px;
    height: 1023px;
    overflow: hidden;
    background: var(--backdrop);
  }
  .canvas {
    position: relative;
    width: 1200px;
    height: 1023px;
  }
  .business-card {
    position: absolute;
    left: 150px;
    top: 254px;
    width: 900px;
    height: 514px;
    background: var(--paper);
    overflow: hidden;
    box-shadow: 0 14px 40px rgba(0, 0, 0, 0.18), 0 2px 6px rgba(0, 0, 0, 0.12);
  }
  .card-swoosh {
    position: absolute;
    inset: 0;
    width: 100%;
    height: 100%;
  }
  .swoosh-teal { fill: var(--teal); }
  .swoosh-dark { fill: var(--ink); }

  .holder {
    position: absolute;
    right: 150px;
    top: 72px;
    text-align: right;
  }
  .holder-name {
    font-family: "Montserrat", sans-serif;
    font-weight: 700;
    font-size: 40px;
    color: var(--teal);
    line-height: 1;
  }
  .holder-role {
    font-family: "Montserrat", sans-serif;
    font-weight: 400;
    font-size: 30px;
    color: var(--ink-soft);
    margin-top: 2px;
    line-height: 1;
  }

  .brand {
    position: absolute;
    left: 130px;
    top: 180px;
    display: flex;
    align-items: center;
    gap: 14px;
  }
  .brand-mark {
    width: 22px;
    height: 22px;
    background: var(--teal);
  }
  .brand-name {
    font-family: "Montserrat", sans-serif;
    font-weight: 600;
    font-size: 30px;
    letter-spacing: 1px;
    color: var(--ink);
    text-transform: uppercase;
  }

  .contact-list {
    position: absolute;
    left: 130px;
    top: 245px;
    list-style: none;
  }
  .contact-item {
    display: flex;
    align-items: center;
    gap: 14px;
    font-family: "Roboto", sans-serif;
    font-weight: 300;
    font-size: 23px;
    color: var(--ink);
    line-height: 1.35;
  }
  .contact-icon {
    width: 20px;
    height: 20px;
    flex: none;
  }
  .contact-icon .stroke { fill: none; stroke: var(--teal); stroke-width: 2; }
  .contact-icon .fill { fill: var(--teal); }
</style>
</head>
<body>
<main class="canvas">
  <article class="business-card">
    <svg class="card-swoosh" viewBox="0 0 900 514" preserveAspectRatio="none" aria-hidden="true">
      <path class="swoosh-teal" d="M0 415 C 450 415 770 370 900 300 L900 514 L0 514 Z"/>
      <path class="swoosh-dark" d="M0 458 C 500 458 800 440 900 400 L900 514 L0 514 Z"/>
    </svg>

    <header class="holder">
      <p class="holder-name">Your Name</p>
      <p class="holder-role">Position</p>
    </header>

    <div class="brand">
      <span class="brand-mark"></span>
      <span class="brand-name">Pinecrest Renovations</span>
    </div>

    <ul class="contact-list">
      <li class="contact-item">
        <svg class="contact-icon" viewBox="0 0 20 20" aria-hidden="true">
          <rect class="stroke" x="4" y="2" width="12" height="16" rx="2"/>
          <rect class="fill" x="8" y="14.5" width="4" height="1.5"/>
        </svg>
        <span>1234 567 891</span>
      </li>
      <li class="contact-item">
        <svg class="contact-icon" viewBox="0 0 20 20" aria-hidden="true">
          <rect class="stroke" x="2" y="4" width="16" height="12"/>
          <path class="stroke" d="M2 4 L10 11 L18 4"/>
        </svg>
        <span>info@pinecrestrenovations.com</span>
      </li>
      <li class="contact-item">
        <svg class="contact-icon" viewBox="0 0 20 20" aria-hidden="true">
          <circle class="fill" cx="10" cy="10" r="9"/>
          <path d="M1 10 H19 M10 1 C 5 5 5 15 10 19 M10 1 C 15 5 15 15 10 19" fill="none" stroke="#fff" stroke-width="1.3"/>
        </svg>
        <span>www.pinecrestrenovations.com</span>
      </li>
    </ul>
  </article>
</main>
</body>
</html>
```